Quarry Vale Business Cards

We need to design some upbeat business cards. We are an Industrial Rope Access Company/Height Safety Company that specialize in Rope Access, Confined Space, Anchor Points, Safety Systems, PPE Inspecions and Rigging.
Company name is Quarry Vale Ltd
Card is for Reggie Stanton the Company Director
His mobile number is 027 816 4920 and email is reggie@quarryvale.co.nz. Website address is www.quarryvale.co.nz.
We will post some pictures below to ensure you get a good idea of what we do.

```html
<!DOCTYPE html>
<html lang="en">
<head>
<meta charset="utf-8">
<title>Quarry Vale Business Cards</title>
<link rel="stylesheet" href="https://fonts.googleapis.com/css2?family=Lato:wght@300;400;700;900&display=swap">
<style>
  :root {
    --backdrop: #4b6374;
    --card: #ffffff;
    --ink: #1c1c1c;
    --ink-soft: #333333;
    --ink-muted: #5a5a5a;
    --band: #111111;
    --band-text: #ffffff;
  }
  * { margin: 0; padding: 0; box-sizing: border-box; }
  html, body { width: 1200px; height: 1000px; overflow: hidden; }
  body {
    background: var(--backdrop);
    font-family: "Lato", sans-serif;
    position: relative;
  }
  .card {
    position: absolute;
    left: 264px;
    width: 672px;
    height: 383px;
    background: var(--card);
    border-radius: 40px;
    overflow: hidden;
  }
  .card--front { top: 85px; }
  .card--back { top: 530px; }

  .front-rule {
    position: absolute;
    top: 189px;
    height: 4px;
    background: var(--ink);
  }
  .front-rule--left { left: 0; width: 108px; }
  .front-rule--right { right: 0; width: 110px; }
  .front-wordmark {
    position: absolute;
    top: 155px;
    left: 0;
    width: 100%;
    text-align: center;
    font-size: 54px;
    font-weight: 900;
    color: var(--ink);
    line-height: 1;
  }

  .holder-name {
    position: absolute;
    left: 43px;
    top: 112px;
    font-size: 36px;
    font-weight: 400;
    color: var(--ink-soft);
    line-height: 1;
  }
  .holder-role {
    position: absolute;
    left: 43px;
    top: 158px;
    font-size: 20px;
    font-weight: 300;
    color: var(--ink-muted);
    line-height: 1;
  }
  .back-wordmark {
    position: absolute;
    right: 60px;
    top: 150px;
    font-size: 34px;
    font-weight: 900;
    color: var(--ink);
    line-height: 1;
  }
  .back-graphics {
    position: absolute;
    left: 0;
    top: 0;
    width: 672px;
    height: 383px;
  }
  .web-address {
    position: absolute;
    left: 416px;
    top: 207px;
    font-size: 19px;
    font-weight: 400;
    color: var(--band-text);
    line-height: 1;
    letter-spacing: 0.2px;
  }
  .contact-list {
    position: absolute;
    left: 43px;
    top: 246px;
    list-style: none;
  }
  .contact-item {
    display: flex;
    align-items: center;
    height: 36px;
    font-size: 24px;
    font-weight: 400;
    color: var(--ink-soft);
  }
  .contact-icon {
    width: 20px;
    height: 20px;
    margin-right: 15px;
    fill: var(--ink-soft);
  }
</style>
</head>
<body>

  <section class="card card--front" aria-label="Business card front">
    <div class="front-rule front-rule--left"></div>
    <div class="front-wordmark">Quarry Vale</div>
    <div class="front-rule front-rule--right"></div>
  </section>

  <section class="card card--back" aria-label="Business card back">
    <svg class="back-graphics" viewBox="0 0 672 383" aria-hidden="true">
      <rect x="43" y="201" width="300" height="2" fill="#1c1c1c"/>
      <path d="M336 202 H672 V235 H362 Q350 235 346 225 Z" fill="#111111"/>
    </svg>
    <div class="holder-name">Reggie Stanton</div>
    <div class="holder-role">Director -&nbsp; Quarry Vale Ltd</div>
    <div class="back-wordmark">Quarry Vale</div>
    <div class="web-address">www.quarryvale.co.nz</div>
    <ul class="contact-list">
      <li class="contact-item">
        <svg class="contact-icon" viewBox="0 0 24 24" aria-hidden="true">
          <path d="M6.6 10.8c1.4 2.8 3.8 5.1 6.6 6.6l2.2-2.2c.3-.3.7-.4 1-.2 1.1.4 2.3.6 3.6.6.6 0 1 .4 1 1V20c0 .6-.4 1-1 1C10.6 21 3 13.4 3 4c0-.6.4-1 1-1h3.5c.6 0 1 .4 1 1 0 1.3.2 2.5.6 3.6.1.3 0 .7-.2 1L6.6 10.8z"/>
        </svg>
        027 816 4920
      </li>
      <li class="contact-item">
        <svg class="contact-icon" viewBox="0 0 24 24" aria-hidden="true">
          <path d="M2 6h20v12H2z M2 6l10 7 10-7" fill="none" stroke="#333" stroke-width="0"/>
          <path d="M2 6h20v1.2l-10 6.6L2 7.2z"/>
          <path d="M2 9l10 6.5L22 9v9H2z"/>
        </svg>
        reggie@quarryvale.co.nz
      </li>
    </ul>
  </section>

</body>
</html>
```